Reef Glow

sunglasses, sihoullette of body, maybe wearing a bikini or sunglasses. I am offering spray tanning, body wraps, tanning beds, stand up, body art, airbrush makeup.

Target Market(s)

I would say my target is all ages, But tanning is a seasonal business and more beauty and aging concept. and around prom time I get my most profitable business. so 18 to 21 through march and april. then 25 to 55 through april to june.

Industry/Entity Type

Makeup

Contact Information for Business Card

Phone number: 701-238-5147 Owner: Jan Porvik (Lindqvast)

Colors

Designer to choose colors to be used in the design.

Requirements
Nice to have
• Sunglasses, silouttes of body wearing sunglasses or bikini, or picture of spray gun.

```html
<!DOCTYPE html>
<html lang="en">
<head>
<meta charset="utf-8">
<title>Reef Glow – Business Card</title>
<link href="https://fonts.googleapis.com/css2?family=Uncial+Antiqua&family=Federo&display=swap" rel="stylesheet">
<style>
  :root {
    --backdrop: #e9e9e9;
    --card: #ffffff;
    --orange: #e8641c;
    --orange-soft: #f07c2c;
    --sun-core: #f5cba4;
    --sun-rays: #fbe3c8;
    --silhouette: #111111;
    --bikini: #f07a22;
  }
  * { margin: 0; padding: 0; box-sizing: border-box; }
  html, body {
    width: 1200px; height: 900px; overflow: hidden;
    background: var(--backdrop);
  }
  .business-card {
    position: absolute; left: 75px; top: 150px;
    width: 1050px; height: 600px;
    background: var(--card);
    box-shadow: 0 6px 24px rgba(0,0,0,.18);
    overflow: hidden;
  }
  .figure-art {
    position: absolute; left: 70px; top: 110px;
    width: 240px; height: 490px;
    background: linear-gradient(180deg, var(--silhouette) 0%, var(--silhouette) 38%, var(--bikini) 42%, var(--silhouette) 50%, var(--silhouette) 70%, var(--bikini) 74%, var(--silhouette) 82%);
    border-radius: 110px 110px 30px 30px;
  }
  .sun-art {
    position: absolute; left: 775px; top: 25px;
    width: 230px; height: 230px; border-radius: 50%;
    background: radial-gradient(circle, var(--sun-core) 0%, var(--sun-core) 45%, var(--sun-rays) 60%, rgba(251,227,200,0) 72%);
  }
  .brand-name {
    position: absolute; left: 300px; top: 70px;
    font-family: "Uncial Antiqua", serif;
    font-size: 76px; color: var(--orange);
    letter-spacing: 1px; line-height: 1;
    white-space: nowrap;
  }
  .owner-block {
    position: absolute; left: 350px; top: 170px;
    font-family: "Federo", sans-serif;
    color: var(--orange-soft);
    font-size: 30px; line-height: 1.25;
    text-transform: uppercase; letter-spacing: 1px;
    white-space: nowrap;
  }
  .owner-block .label { padding-left: 70px; }
  .contact-row { display: flex; gap: 14px; }
  .contact-row .key { width: 140px; white-space: pre; }
  .services {
    position: absolute; left: 330px; top: 340px;
    width: 700px; height: 200px;
    font-family: "Federo", sans-serif;
    color: var(--orange);
    font-size: 20px; text-transform: uppercase; letter-spacing: .5px;
    list-style: none;
  }
  .services li { position: absolute; display: flex; align-items: center; gap: 12px; white-space: nowrap; }
  .services li::before {
    content: ""; width: 12px; height: 12px; border-radius: 50%;
    background: var(--silhouette);
  }
  .svc-tanning-beds { left: 420px; top: 0; }
  .svc-airbrush { left: 420px; top: 38px; }
  .svc-body-wraps { left: 250px; top: 50px; }
  .svc-body-art { left: 250px; top: 98px; }
  .svc-spray { left: 0; top: 130px; }
  .svc-stand-up { left: 0; top: 172px; }
</style>
</head>
<body>
  <section class="business-card">
    <div class="sun-art" role="img" aria-label="Peach sun with rays wearing dark sunglasses"></div>
    <div class="figure-art" role="img" aria-label="Black silhouette of a woman in an orange bikini"></div>
    <h1 class="brand-name">Reef Glow</h1>
    <div class="owner-block">
      <div class="label">Owner :</div>
      <div>Jan Porvik (Lindqvast)</div>
      <div class="contact-row"><span class="key">Phone :</span><span>(701) 238-5147</span></div>
      <div class="contact-row"><span class="key">Cell    :</span><span>(701) 238-5190.</span></div>
    </div>
    <ul class="services">
      <li class="svc-tanning-beds">Tanning beds.</li>
      <li class="svc-airbrush">Airbrush makeup.</li>
      <li class="svc-body-wraps">Body wraps.</li>
      <li class="svc-body-art">Body art.</li>
      <li class="svc-spray">Spray tanning.</li>
      <li class="svc-stand-up">Stand up.</li>
    </ul>
  </section>
</body>
</html>
```